Consulting Company needs business card design

We need a business card design for a new consulting and business solutions company based in Bermuda called Corvane Holdings Limited. Looking for a double sided business card with one side only including the company logo thats attached and the other including contact information. Logo contains blue and turquoise colors and is fine to be on both sides of the card.
Contact Information for Business Card
Corvane Holdings Limited
P.O. Box KR318
Pemberly KR LT
Bermuda
Name: Marcus Telford
Position: Director
Telephone: 1 441 732 4590
Email: mtelford@corvane.bm
Website: www.corvane.bm

```html
<!DOCTYPE html>
<html lang="en">
<head>
<meta charset="UTF-8">
<title>Corvane Holdings Limited — Business Card</title>
<link href="https://fonts.googleapis.com/css2?family=Roboto:wght@400;500;700&display=swap" rel="stylesheet">
<style>
  :root {
    --backdrop: #3b3430;
    --card-dark: #151515;
    --card-light: #ffffff;
    --brand-blue: #2a9fdc;
    --brand-turquoise: #18adbd;
    --ink: #3a3a3a;
    --rule: #9a9a9a;
  }
  * { margin: 0; padding: 0; box-sizing: border-box; }
  html, body {
    width: 1200px; height: 870px; overflow: hidden;
    background: var(--backdrop);
    font-family: "Roboto", sans-serif;
  }
  .card {
    position: absolute;
    width: 560px; height: 320px;
    border-radius: 6px;
    overflow: hidden;
    box-shadow: 0 10px 24px rgba(0,0,0,.45);
  }
  .card--front {
    left: 60px; top: 90px;
    background: var(--card-dark);
    border-bottom: 6px solid var(--brand-blue);
    display: flex; align-items: center; justify-content: center; gap: 16px;
  }
  .brand-mark {
    width: 40px; height: 40px; border-radius: 50%;
    background: var(--brand-blue);
    flex: none;
  }
  .brand-name {
    font-weight: 500;
    color: var(--brand-blue);
    text-transform: uppercase;
    letter-spacing: 2px;
    line-height: 1.1;
  }
  .card--front .brand-name { font-size: 30px; }

  .card--back {
    left: 580px; top: 460px;
    background: var(--card-light);
  }
  .card--back .brand {
    position: absolute; left: 40px; top: 116px;
    display: flex; align-items: center; gap: 12px;
  }
  .card--back .brand-mark { width: 30px; height: 30px; background: var(--brand-turquoise); }
  .card--back .brand-name { font-size: 17px; color: var(--brand-turquoise); letter-spacing: 1px; width: 190px; }
  .divider {
    position: absolute; left: 282px; top: 70px;
    width: 1px; height: 150px; background: var(--rule);
  }
  .contact {
    position: absolute; left: 306px; top: 66px;
    color: var(--ink); font-size: 13px; line-height: 1.45;
  }
  .contact__name { color: var(--brand-turquoise); font-weight: 700; font-size: 21px; line-height: 1.1; }
  .contact__role { font-weight: 500; margin-bottom: 8px; }
  .contact__address { margin-bottom: 6px; }
  .contact__line { display: flex; align-items: center; gap: 8px; }
  .contact__line svg { width: 13px; height: 13px; flex: none; }
  .base-band {
    position: absolute; left: 0; right: 0; bottom: 0; height: 26px;
    background: var(--brand-turquoise);
  }
  .base-band::before {
    content: ""; position: absolute; left: 0; right: 0; top: 6px;
    height: 2px; background: var(--card-light);
  }
</style>
</head>
<body>
  <section class="card card--front" aria-label="Card front">
    <span class="brand-mark" aria-hidden="true"></span>
    <span class="brand-name">Corvane Holdings Limited</span>
  </section>

  <section class="card card--back" aria-label="Card back">
    <div class="brand">
      <span class="brand-mark" aria-hidden="true"></span>
      <span class="brand-name">Corvane Holdings Limited</span>
    </div>
    <div class="divider"></div>
    <div class="contact">
      <p class="contact__name">Marcus Telford</p>
      <p class="contact__role">Director</p>
      <p class="contact__address">P.O. Box KR318<br>Pemberly KR LT, Bermuda</p>
      <p class="contact__line">
        <svg viewBox="0 0 16 16" aria-hidden="true"><path d="M4 1l3 3-2 2c1 2 3 4 5 5l2-2 3 3-2 2C7 14 2 9 2 3z" fill="var(--brand-turquoise)"/></svg>
        1 441 732 4590
      </p>
      <p class="contact__line">
        <svg viewBox="0 0 16 16" aria-hidden="true"><rect x="1" y="3" width="14" height="10" fill="none" stroke="var(--brand-turquoise)" stroke-width="1.4"/><path d="M1 3l7 6 7-6" fill="none" stroke="var(--brand-turquoise)" stroke-width="1.4"/></svg>
        mtelford@corvane.bm
      </p>
      <p class="contact__line">
        <svg viewBox="0 0 16 16" aria-hidden="true"><g fill="none" stroke="var(--brand-turquoise)" stroke-width="1.2"><circle cx="8" cy="8" r="6.5"/><ellipse cx="8" cy="8" rx="3" ry="6.5"/><path d="M1.5 8h13M2.5 4.5h11M2.5 11.5h11"/></g></svg>
        www.corvane.bm
      </p>
    </div>
    <div class="base-band"></div>
  </section>
</body>
</html>
```